Health care technology software systems

We have a solid logo. We have company colors that will need to be used as well. We just need a great business card design. We sell to health plans but want to be modern

Target Market(s)

Health technology sector selling into Health Plans

Industry/Entity Type

Health Care Technology

Contact Information for Business Card

Name, title, address, phone number, email

Requirements
Must have
• Use of Parvexa corporate colors - Uploaded w/ our logos

```html
<!DOCTYPE html>
<html lang="en">
<head>
<meta charset="utf-8">
<title>Parvexa Business Card</title>
<link rel="stylesheet" href="https://fonts.googleapis.com/css2?family=Raleway:wght@300&family=Roboto:wght@400;500;700&display=swap">
<style>
  :root {
    --backdrop: #e6e7ea;
    --card: #ffffff;
    --card-dark: #222224;
    --pattern-light: #3a3a3d;
    --ink: #2b2b2e;
    --brand-blue: #3a5fae;
    --sky-blue: #1a9fdc;
    --leaf-green: #7cc242;
  }
  * { margin: 0; padding: 0; box-sizing: border-box; }
  html, body {
    width: 1200px; height: 900px; overflow: hidden;
    background: var(--backdrop);
  }
  .canvas { position: relative; width: 1200px; height: 900px; }
  .card {
    position: absolute; left: 240px;
    width: 720px; height: 411px;
    border-radius: 26px;
    overflow: hidden;
    box-shadow: 0 8px 24px rgba(0,0,0,0.16);
  }
  .card-front { top: 28px; background: var(--card); }
  .card-back { top: 467px; background: var(--card-dark); }

  .card-swoosh { position: absolute; inset: 0; width: 100%; height: 100%; }
  .brand {
    position: absolute; left: 56px; top: 98px;
    display: flex; align-items: center; gap: 16px;
  }
  .brand-dot {
    width: 42px; height: 42px; border-radius: 50%;
    background: var(--brand-blue);
  }
  .brand-name {
    font-family: "Raleway", sans-serif; font-weight: 300;
    font-size: 66px; line-height: 1; color: var(--ink);
    letter-spacing: 1px;
  }
  .divider {
    position: absolute; left: 403px; top: 160px;
    width: 1.5px; height: 150px; background: var(--brand-blue);
  }
  .contact {
    position: absolute; left: 426px; top: 154px;
    font-family: "Roboto", sans-serif; color: var(--ink);
  }
  .contact-name {
    font-weight: 700; font-size: 24px; letter-spacing: 0.8px;
    text-transform: uppercase; line-height: 1.1;
  }
  .contact-name .first { color: var(--leaf-green); }
  .contact-name .last { color: var(--sky-blue); }
  .contact-title { font-size: 16px; margin-top: 2px; }
  .contact-address { font-size: 16px; line-height: 1.35; margin-top: 8px; }
  .contact-lines { list-style: none; margin-top: 6px; font-size: 15px; line-height: 1.4; }
  .contact-lines li { display: flex; align-items: center; gap: 7px; }
  .contact-lines svg { width: 12px; height: 12px; flex: none; }

  .back-pattern {
    position: absolute; inset: 0;
    background: linear-gradient(135deg, var(--card-dark) 0%, var(--pattern-light) 55%, var(--card-dark) 100%);
  }
  .back-mark {
    position: absolute; right: 38px; bottom: 36px;
    width: 40px; height: 40px; border-radius: 50%;
    background: var(--brand-blue);
  }
</style>
</head>
<body>
<div class="canvas">
  <div class="card card-front">
    <svg class="card-swoosh" viewBox="0 0 1000 572" preserveAspectRatio="none" aria-hidden="true">
      <path d="M0 318 C 170 420, 520 540, 1000 540 L 1000 572 L 0 572 Z" fill="var(--brand-blue)"/>
      <path d="M300 432 C 520 500, 760 510, 1000 500 L 1000 512 C 760 522, 520 512, 300 432 Z" fill="var(--sky-blue)"/>
      <path d="M300 436 C 520 514, 760 524, 1000 518 L 1000 530 C 760 536, 520 526, 300 436 Z" fill="var(--leaf-green)"/>
    </svg>

    <div class="brand">
      <div class="brand-dot"></div>
      <div class="brand-name">parvexa</div>
    </div>

    <div class="divider"></div>

    <div class="contact">
      <div class="contact-name"><span class="first">Dorian</span> <span class="last">Hale</span></div>
      <div class="contact-title">Owner/CEO</div>
      <div class="contact-address">1480 Wexford Avenue<br>Calder County 6142</div>
      <ul class="contact-lines">
        <li>
          <svg viewBox="0 0 16 16"><path d="M4 1.5 L6.5 4.5 L5 6.5 C6 8.5 7.5 10 9.5 11 L11.5 9.5 L14.5 12 L12.5 14.5 C7 14 2 9 1.5 3.5 Z" fill="var(--sky-blue)"/></svg>
          555-014-2876
        </li>
        <li>
          <svg viewBox="0 0 16 16"><rect x="1" y="3" width="14" height="10" fill="var(--sky-blue)"/><path d="M1 3 L8 9 L15 3" fill="none" stroke="#fff" stroke-width="1.4"/></svg>
          info@parvexa.com
        </li>
        <li>
          <svg viewBox="0 0 16 16"><circle cx="8" cy="8" r="7" fill="var(--sky-blue)"/><path d="M1 8 H15 M8 1 C4 5 4 11 8 15 M8 1 C12 5 12 11 8 15" fill="none" stroke="#fff" stroke-width="1"/></svg>
          www.parvexa.com
        </li>
      </ul>
    </div>
  </div>

  <div class="card card-back">
    <div class="back-pattern" role="img" aria-label="Repeating tonal ring pattern in dark grey gloss across the card back"></div>
    <div class="back-mark"></div>
  </div>
</div>
</body>
</html>
```